Move the hackers to Wordpress

Yep, we want to move https://www.tallowmarsh.com/ to Wordpress. It'll make it easier to update and add content. I'd like mostly the same look, but I'm not stuck with it.
Updates

DO NOT RESPOND OUTSIDE OF PIXEL HARBOR OR CONTACT US DIRECTLY.

Industry/Entity Type

Computer Security

Coding

Coded - Design and coding required

Font styles to use
Sans Serif

Colors
ec1f27

Requirements
Must have
• What I do want is:
• 1. Similar look to the existing site
• 2. Needs to work on one of the Wordpress hosting sites. I do NOT want to run my own Wordpress server.
• 3. Keep the animation in the top panel.
• 4. Mobile support
• The rest can be changed as needed.
Nice to have
• I like the transitions when the "services" panel shows up. Not stuck on it, but it is a nice touch.

```html
<!DOCTYPE html>
<html lang="en">
<head>
<meta charset="utf-8">
<title>Tallow Marsh — Offensive Services From Offensive Minds</title>
<link rel="stylesheet" href="https://fonts.googleapis.com/css2?family=Montserrat:wght@400;600;700;800&family=Overpass:wght@300;400;600;700&display=swap">
<style>
:root{
  --red:#ec1f27;
  --red-deep:#c8141b;
  --red-light:#f0323a;
  --ink:#2b2b2b;
  --text:#6b6b6b;
  --grey-bg:#ececec;
  --navy:#2c2f3d;
  --navy-deep:#1f2230;
  --footer:#23252f;
  --footer-bottom:#1a1c24;
  --white:#ffffff;
  --line:#d9d9d9;
}
*{margin:0;padding:0;box-sizing:border-box}
html,body{width:1200px;height:4932px;overflow:hidden}
body{position:relative;font-family:"Overpass",Arial,sans-serif;color:var(--text);background:var(--white)}
.heading{font-family:"Montserrat",Arial,sans-serif}
section,header,footer{position:absolute;left:0;width:1200px}

/* Hero */
.hero{top:0;height:516px;overflow:hidden}
.hero-bg{position:absolute;inset:0;background:radial-gradient(ellipse at 30% 40%,#3b3b3f 0%,#1b1b1e 55%,#0c0c0d 100%)}
.brand{position:absolute;display:flex;align-items:center;gap:10px;font-family:"Montserrat",Arial,sans-serif;font-weight:800;color:var(--white);letter-spacing:1px}
.brand-mark{width:18px;height:18px;background:var(--red)}
.hero .brand{left:82px;top:56px;font-size:20px}
.nav{position:absolute;top:62px;right:64px;display:flex;gap:30px;align-items:center;font-family:"Montserrat",Arial,sans-serif;font-size:13px;font-weight:600;color:var(--white);letter-spacing:.5px}
.nav .active{color:var(--red)}
.hero-title{position:absolute;left:58px;top:196px;font-family:"Montserrat",Arial,sans-serif;font-weight:800;font-size:50px;line-height:60px;color:var(--white);letter-spacing:1px}
.hero-title em{font-style:normal;color:var(--red)}
.scroll-cue{position:absolute;left:582px;top:444px;width:22px;height:36px;border:2px solid var(--white);border-radius:11px}
.scroll-cue::after{content:"";position:absolute;left:8px;top:7px;width:2px;height:8px;background:var(--white)}

/* What we do */
.what{top:516px;height:569px;background:var(--grey-bg);overflow:hidden}
.what svg.diag{position:absolute;inset:0}
.section-title{font-family:"Montserrat",Arial,sans-serif;font-size:32px;font-weight:400;color:var(--ink);letter-spacing:2px}
.section-title b{font-weight:800}
.what .section-title{position:absolute;left:82px;top:72px}
.what .lead{position:absolute;left:82px;top:188px;width:680px;font-size:19px;color:var(--ink)}
.what .body{position:absolute;left:82px;top:236px;width:680px;font-size:18px;line-height:32px;color:var(--text)}
.emblem{position:absolute;left:900px;top:130px;width:120px;height:120px;background:var(--red);display:flex;align-items:center;justify-content:center;font-family:"Montserrat",Arial,sans-serif;font-weight:800;font-size:14px;color:var(--white);text-align:center;line-height:18px}

/* Services */
.services{top:1085px;height:1184px;background:var(--red);overflow:hidden}
.services svg.diag{position:absolute;inset:0}
.services .section-title{position:absolute;left:0;width:1200px;top:118px;text-align:center;color:var(--white);font-size:44px}
.service{position:absolute;width:330px;text-align:center;color:var(--white)}
.service svg{display:block;margin:0 auto 30px;width:84px;height:84px}
.service h3{font-family:"Montserrat",Arial,sans-serif;font-size:14px;font-weight:700;line-height:17px;margin-bottom:12px;letter-spacing:.3px}
.service p{font-size:14px;line-height:21px}

/* About */
.about{top:2269px;height:631px;background:var(--white)}
.about .section-title{position:absolute;left:82px;top:84px}
.about-rule{position:absolute;left:82px;top:138px;width:40px;height:3px;background:var(--red)}
.about p{position:absolute;left:82px;top:180px;width:480px;font-size:20px;line-height:34px;color:var(--ink)}
.laptop{position:absolute;left:658px;top:100px;width:430px;height:312px;background:linear-gradient(180deg,#1a1a1a 0%,#0a0a0a 88%,#cfcfcf 88%,#9a9a9a 100%);border-radius:12px 12px 4px 4px}

/* Testimonial */
.testimonial{top:2900px;height:536px;background:linear-gradient(160deg,var(--navy) 0%,var(--navy-deep) 100%)}
.avatar{position:absolute;left:526px;top:76px;width:144px;height:144px;border-radius:50%;background:radial-gradient(circle at 50% 40%,#d9b99b 0%,#a78468 60%,#e9e9ee 61%);border:4px solid var(--white)}
.t-name{position:absolute;left:0;width:1200px;top:262px;text-align:center;font-family:"Montserrat",Arial,sans-serif;font-size:13px;font-weight:700;color:var(--white)}
.t-role{position:absolute;left:0;width:1200px;top:284px;text-align:center;font-size:12px;color:#b8bac4}
.t-quote{position:absolute;left:0;width:1200px;top:318px;text-align:center;font-size:19px;color:#7d8090}
.arrow{position:absolute;top:222px;width:20px;height:20px}

/* Contact */
.contact{top:3436px;height:1003px;background:var(--white)}
.contact-title{position:absolute;left:0;width:1200px;top:98px;text-align:center;font-family:"Montserrat",Arial,sans-serif;font-weight:800;font-size:46px;line-height:68px;color:var(--red);letter-spacing:1px}
.contact-intro{position:absolute;left:300px;width:600px;top:240px;text-align:center;font-size:13px;line-height:20px;color:var(--text)}
.field{position:absolute;height:46px;border:1px solid var(--line);background:#f7f7f7;font-size:13px;color:#999;padding:14px 16px}
.field.area{height:352px}
.field span{position:absolute;right:14px;top:14px;width:14px;height:14px;border:1.5px solid #aaa;border-radius:3px}
.submit{position:absolute;left:82px;top:789px;width:1036px;height:43px;background:var(--red);color:var(--white);font-family:"Montserrat",Arial,sans-serif;font-weight:700;font-size:15px;text-align:center;line-height:43px;letter-spacing:.5px}

/* Footer */
.footer{top:4439px;height:394px;background:var(--footer);color:#c9cbd3}
.footer .brand{left:82px;top:36px;font-size:22px}
.footer .tag{position:absolute;left:82px;top:180px;font-family:"Montserrat",Arial,sans-serif;font-weight:800;font-size:21px;line-height:40px;color:var(--white)}
.footer .tag em{font-style:normal;color:var(--red)}
.col-title{position:absolute;top:40px;font-family:"Montserrat",Arial,sans-serif;font-weight:700;font-size:17px;color:var(--white)}
.col-title::after{content:"";display:inline-block;width:5px;height:5px;background:var(--red);margin-left:6px;vertical-align:middle}
.contact-line{position:absolute;left:437px;font-size:13px;display:flex;gap:12px;align-items:center}
.contact-line em{font-style:normal;color:var(--red)}
.links{position:absolute;left:796px;top:86px;width:322px;list-style:none;font-size:13px}
.links li{height:56px;line-height:56px;border-bottom:1px solid #34374a}
.bottom-bar{position:absolute;left:0;top:4833px;width:1200px;height:99px;background:var(--footer-bottom);font-size:12px;color:#8b8e9a}
.bottom-bar .copy{position:absolute;left:82px;top:42px}
.bottom-bar .link{position:absolute;top:42px}
.dots{position:absolute;left:972px;top:44px;display:flex;gap:10px}
.dots i{width:10px;height:10px;border-radius:50%;background:#4b7bd0;display:block}
.to-top{position:absolute;left:1112px;top:10px;width:40px;height:40px;background:#111218;border-radius:50%}
</style>
</head>
<body>

<header class="hero">
  <div class="hero-bg" role="img" aria-label="Dark low-poly faceted background with glowing red points"></div>
  <div class="brand"><span class="brand-mark"></span>TALLOW MARSH</div>
  <nav class="nav">
    <span class="active">WHAT WE DO</span><span>ABOUT US</span><span>SERVICES</span><span>BLOG</span><span>PRESS</span><span>CONTACT US</span>
    <svg width="14" height="14" viewBox="0 0 14 14" fill="none" stroke="#fff" stroke-width="1.6"><circle cx="6" cy="6" r="4.5"/><path d="M9.5 9.5L13 13"/></svg>
  </nav>
  <h1 class="hero-title"><em>OFFENSIVE</em> SERVICES<br>FROM <em>OFFENSIVE</em> MINDS</h1>
  <div class="scroll-cue"></div>
</header>

<section class="what">
  <svg class="diag" width="1200" height="569" viewBox="0 0 1200 569"><polygon points="1200,0 1200,569 900,569" fill="#ffffff"/></svg>
  <h2 class="section-title">WHAT WE <b>DO</b></h2>
  <p class="lead">We are an information security company focusing on real world threats.</p>
  <p class="body">Tallow Marsh is an information security consulting company that concentrates on the latest threats to organizations today. We perform in-depth analysis, determine organization/business risk, and find the vulnerabilities before the bad guys do. Our team includes internationally renowned experts who have been featured in international news outlets and conferences, including The Harbor Ledger, The Capital Courier, an Eastline News Documentary.</p>
  <div class="emblem">TALLOW<br>MARSH</div>
</section>

<section class="services">
  <svg class="diag" width="1200" height="1184" viewBox="0 0 1200 1184"><polygon points="1200,0 1200,1184 560,1184" fill="#e0161e"/><polygon points="1200,380 1200,1184 820,1184" fill="#d3131a"/></svg>
  <h2 class="section-title">OUR <b>SERVICES</b></h2>

  <div class="service" style="left:65px;top:247px">
    <svg viewBox="0 0 84 84" fill="none" stroke="#fff" stroke-width="8"><path d="M22 30a26 26 0 1 1-2 26"/><path d="M10 18v18h18" stroke-width="7"/></svg>
    <h3>INTERNAL PIVOT ASSESSMENT &amp;<br>POST EXPLOITATION</h3>
    <p>We start as a low privilege user and attempt to move through the network in an attempt to access the data that matters to you. This is a simulation of a rogue trusted insider or a compromised internal host. We determine your risk when the egg shell is cracked.</p>
  </div>
  <div class="service" style="left:433px;top:247px">
    <svg viewBox="0 0 84 84" fill="#fff"><circle cx="42" cy="24" r="13"/><path d="M20 70c0-16 10-26 22-26s22 10 22 26z"/><circle cx="18" cy="32" r="9"/><path d="M2 66c0-12 7-19 16-19 4 0 7 1 9 3-4 5-6 10-6 16z"/><circle cx="66" cy="32" r="9"/><path d="M82 66c0-12-7-19-16-19-4 0-7 1-9 3 4 5 6 10 6 16z"/></svg>
    <h3>RED TEAM ADVERSARY<br>SIMULATION</h3>
    <p>A goal-based assessment where we attack just like a real world adversary. This includes external attacks and targeted phishing to demonstrate the real risk to your data.</p>
  </div>
  <div class="service" style="left:811px;top:247px">
    <svg viewBox="0 0 84 84" fill="#fff"><circle cx="30" cy="46" r="20"/><g stroke="#fff" stroke-width="9"><path d="M30 18v56M2 46h56M10 26l40 40M50 26L10 66"/></g><circle cx="30" cy="46" r="8" fill="#ec1f27"/><circle cx="66" cy="20" r="11"/><g stroke="#fff" stroke-width="5"><path d="M66 4v32M50 20h32M55 9l22 22M77 9L55 31"/></g><circle cx="66" cy="20" r="4" fill="#ec1f27"/></svg>
    <h3>PENETRATION TESTING &amp;<br>VULNERABILITY ASSESSMENTS</h3>
    <p>This includes vulnerability scans of the in-scope systems where we manually verify issues and exploit any issues found. We report on the issues that actually have a real risk to your organization.</p>
  </div>

  <div class="service" style="left:65px;top:756px">
    <svg viewBox="0 0 84 84" fill="none" stroke="#fff" stroke-width="6"><rect x="22" y="6" width="40" height="72" rx="6"/><circle cx="42" cy="66" r="2" fill="#fff"/></svg>
    <h3>MOBILE APPLICATION<br>ASSESSMENT</h3>
    <p>We look at your mobile application and the associated infrastructure to find configuration weaknesses, server-side issues, insecure authentication and access control, and other issues related to the latest attacks on mobile applications.</p>
  </div>
  <div class="service" style="left:433px;top:756px">
    <svg viewBox="0 0 84 84" fill="none" stroke="#fff" stroke-width="8"><path d="M4 24h16c18 0 24 36 42 36h10M4 60h16c8 0 13-7 17-15M48 34c4-6 8-10 14-10h10"/><path d="M68 12l12 12-12 12M68 48l12 12-12 12" stroke-width="6"/></svg>
    <h3>ADVANCED PRODUCT, HARDWARE<br>&amp; RF TESTING</h3>
    <p>This is a highly customized assessment designed for you and your hardware. Depending on the product we will analyze custom RF protocols, reverse engineer OS and firmware, and analyze and fuzz network protocols.</p>
  </div>
  <div class="service" style="left:811px;top:756px">
    <svg viewBox="0 0 84 84" fill="#fff"><circle cx="32" cy="24" r="16"/><path d="M2 78c0-20 13-34 30-34s30 14 30 34z"/><path d="M64 40h8v12h12v8H72v12h-8V60H52v-8h12z" stroke="#ec1f27" stroke-width="3"/></svg>
    <h3>WEB APPLICATION PENETRATION<br>TESTING</h3>
    <p>Our team will perform an in-depth analysis of your web application to find vulnerabilities related to programming errors, misconfiguration, and application architectural issues. We will perform automated and manual runtime analysis of your application.</p>
  </div>
</section>

<section class="about">
  <h2 class="section-title">ABOUT <b>US</b></h2>
  <div class="about-rule"></div>
  <p>We focus on hacking. This is our passion. We find the vulnerabilities before the bad guys do.</p>
  <div class="laptop" role="img" aria-label="Laptop computer with a dark screen"></div>
</section>

<section class="testimonial">
  <svg class="arrow" style="left:24px" viewBox="0 0 20 20" fill="none" stroke="#fff" stroke-width="3"><path d="M13 3L6 10l7 7"/></svg>
  <svg class="arrow" style="left:1156px" viewBox="0 0 20 20" fill="none" stroke="#fff" stroke-width="3"><path d="M7 3l7 7-7 7"/></svg>
  <div class="avatar" role="img" aria-label="Portrait photo of the client"></div>
  <div class="t-name">MARTA OLSEN</div>
  <div class="t-role">Marketing Manager</div>
  <p class="t-quote">I read the report yesterday. This is one of the best-written, actionable pentest reports I've ever seen.</p>
</section>

<section class="contact">
  <h2 class="contact-title">LET'S MAKE SOMETHING<br>TOGETHER</h2>
  <p class="contact-intro">We have a unique story with each client. Tell us about your systems, your risks and your goals, and we will shape an assessment around what matters most to you.</p>
  <div class="field" style="left:82px;top:349px;width:319px">Name*<span></span></div>
  <div class="field" style="left:437px;top:349px;width:319px">Email*<span></span></div>
  <div class="field" style="left:796px;top:349px;width:322px">Website*<span style="border-radius:50%"></span></div>
  <div class="field area" style="left:82px;top:404px;width:1036px">Message*</div>
  <div class="submit">SUBMIT MESSAGE</div>
</section>

<footer class="footer">
  <div class="brand"><span class="brand-mark"></span>TALLOW MARSH</div>
  <p class="tag"><em>OFFENSIVE</em> SERVICES<br>FROM <em>OFFENSIVE</em> MINDS</p>
  <div class="col-title" style="left:437px">CONTACT</div>
  <div class="contact-line" style="top:216px">
    <svg width="12" height="12" viewBox="0 0 12 12" fill="#c9cbd3"><path d="M2 1l2.5 0 1 3-1.5 1c.7 1.5 1.5 2.3 3 3l1-1.5 3 1V11c-5 0-9-4-9-10z"/></svg>
    Phone: +1-555-010-4242</div>
  <div class="contact-line" style="top:250px">
    <svg width="12" height="10" viewBox="0 0 12 10" fill="none" stroke="#c9cbd3" stroke-width="1.2"><rect x=".6" y=".6" width="10.8" height="8.8"/><path d="M.6 .6L6 5.5 11.4.6"/></svg>
    Email: <em>hello@tallowmarsh.com</em></div>
  <div class="col-title" style="left:796px">QUICK LINKS</div>
  <ul class="links"><li>Home</li><li>About Us</li><li>Services</li><li>Contact</li></ul>
</footer>

<div class="bottom-bar">
  <span class="copy">Copyright © 2019 TallowMarsh.</span>
  <span class="link" style="left:528px">Support</span>
  <span class="link" style="left:610px">Disclaimer</span>
  <div class="dots"><i></i><i></i><i></i><i></i><i></i><i></i></div>
  <div class="to-top"></div>
</div>

</body>
</html>
```